Packaging design for handmade soap

We are looking for a packaging design for a brand new product line: handmade soaps, called NALVI

We are looking for a design of an outer box together with the logo. We need the design for a 90x65x30mm box (see attached). We trying to get a high-end product preferable with vintage elements (but we don't want a shiny box, it will be finished with matte lacque, however logo or other certain elements could be shiny).

The design should reflect the fact that we have a handmade, all natural soap.

I uploaded a couple of packaging examples I like.

UPDATE 1: It also should have a title, which describes the product more accurate, like "Natural Soap with Seabuckthorn and Olive oil"

UPDATE 2: I would remove the expression "high-end" from the description if high end would mean a lot of flowers in the background. I would like if you would insist about the ideea of "natural" in your works

UPDATE 3: Prefered colors green and brown (which brings the ideea of nature, natural)

Target Market(s)

Women 20-45 years with above average income

Industry/Entity Type

Cosmetics

Font styles to use
Serif

Colors
9bcb3c
acd036
cadf82
f78f20
ffc214
f37122
fbed22
fece3e
faa54b

Requirements
Must have
• A literal representation of the brand NALVI (we don't have a logo for it)

```html
<!DOCTYPE html>
<html lang="en">
<head>
<meta charset="utf-8">
<title>NALVI Handmade Natural Soap – Box Dieline</title>
<link href="https://fonts.googleapis.com/css2?family=Cinzel:wght@400;500&family=Roboto+Condensed:wght@300&display=swap" rel="stylesheet">
<style>
  :root {
    --brown: #361f05;
    --green: #acd036;
    --green-soft: #cadf82;
    --cream: #f6dfc0;
    --orange: #f78f20;
    --white: #ffffff;
    --paper: #ffffff;
    --cut: #000000;
    --label-green-text: #6f9a1e;
  }
  html, body { margin: 0; padding: 0; width: 1200px; height: 1081px; overflow: hidden; background: var(--paper); }
  .dieline { display: block; width: 1200px; height: 1081px; }
  .panel { fill: var(--brown); stroke: var(--cut); stroke-width: 5; stroke-linejoin: round; }
  .flap { fill: var(--green); stroke: var(--cut); stroke-width: 5; stroke-linejoin: round; }
  .slit { fill: none; stroke: var(--cut); stroke-width: 5; }
  .frame-outer { fill: var(--brown); stroke: var(--white); stroke-width: 4; }
  .frame-green { fill: var(--green); }
  .frame-white { fill: var(--white); }
  .brand { font-family: "Cinzel", serif; font-weight: 500; letter-spacing: 0.04em; }
  .tagline { font-family: "Cinzel", serif; font-weight: 400; letter-spacing: 0.06em; }
  .ingredients { font-family: "Roboto Condensed", sans-serif; font-weight: 300; }
  .on-green .brand { fill: var(--brown); }
  .on-green .tagline, .on-green .ingredients { fill: var(--white); }
  .on-green .rule { stroke: var(--white); }
  .on-white .brand { fill: var(--brown); }
  .on-white .tagline, .on-white .ingredients { fill: var(--label-green-text); }
  .on-white .rule { stroke: var(--label-green-text); }
  .rule { stroke-width: 2; }
  .botanical { opacity: 0.35; }
</style>
</head>
<body>
<svg class="dieline" viewBox="0 0 2030 1828" xmlns="http://www.w3.org/2000/svg" preserveAspectRatio="none">
  <defs>
    <linearGradient id="botanical-tone" x1="0" y1="0" x2="1" y2="1">
      <stop offset="0" stop-color="#cadf82"/>
      <stop offset="0.5" stop-color="#f6dfc0"/>
      <stop offset="1" stop-color="#faa54b"/>
    </linearGradient>
  </defs>

  <!-- tuck flaps -->
  <path class="panel" d="M288,445 V148 C288,60 330,5 360,5 H860 C900,5 930,60 930,148 V445 Z"/>
  <path class="slit" d="M288,148 H348 V178 M348,160 H870 M870,178 V148 H930"/>
  <path class="panel" d="M1222,1333 H1865 V1630 C1865,1720 1830,1775 1790,1775 H1290 C1250,1775 1222,1720 1222,1630 Z"/>
  <path class="slit" d="M1222,1630 H1284 V1600 M1284,1615 H1805 M1805,1600 V1630 H1865"/>

  <!-- dust flaps -->
  <polygon class="flap" points="10,445 10,395 32,375 76,200 268,200 268,425 288,445"/>
  <polygon class="flap" points="930,445 950,425 950,200 1152,200 1197,378 1218,398 1218,445"/>
  <polygon class="flap" points="5,1333 25,1355 25,1580 218,1580 262,1400 284,1380 284,1333"/>
  <polygon class="flap" points="935,1333 935,1380 958,1400 1002,1580 1204,1580 1204,1355 1224,1333"/>
  <polygon class="flap" points="1865,445 2012,490 2012,1285 1865,1333"/>

  <!-- main panels -->
  <rect class="panel side-left" x="5" y="445" width="283" height="888"/>
  <rect class="panel front" x="288" y="445" width="642" height="888"/>
  <rect class="panel side-right" x="930" y="445" width="294" height="888"/>
  <rect class="panel back" x="1224" y="445" width="641" height="888"/>

  <!-- botanical artwork areas -->
  <g class="botanical" role="img" aria-label="Hand-drawn wildflowers, ferns, seed heads, leaves and small birds in cream, green, orange and yellow line art">
    <rect x="300" y="460" width="618" height="860" rx="30" fill="url(#botanical-tone)"/>
  </g>
  <g class="botanical" role="img" aria-label="Hand-drawn wildflowers, ferns, seed heads, leaves and small birds in cream, green, orange and yellow line art">
    <rect x="1234" y="455" width="620" height="865" rx="30" fill="url(#botanical-tone)"/>
  </g>

  <!-- front label -->
  <g class="label on-green">
    <rect class="frame-outer" x="460" y="480" width="295" height="605" rx="70"/>
    <rect class="frame-green" x="485" y="510" width="245" height="545" rx="50"/>
    <g transform="translate(615,770) rotate(-90)">
      <text class="brand" x="80" y="-10" font-size="78" text-anchor="middle">NALVI</text>
      <text class="tagline" x="80" y="22" font-size="20" text-anchor="middle">HANDMADE NATURAL SOAP</text>
      <line class="rule" x1="-35" y1="38" x2="195" y2="38"/>
      <text class="ingredients" x="80" y="72" font-size="24" text-anchor="middle">with Seabuckthorn &amp; Olive oil</text>
    </g>
  </g>

  <!-- back label -->
  <g class="label on-white">
    <rect class="frame-outer" x="1385" y="680" width="325" height="610" rx="70"/>
    <rect class="frame-white" x="1410" y="710" width="275" height="550" rx="50"/>
    <g transform="translate(1548,985) rotate(90)">
      <text class="brand" x="100" y="-2" font-size="78" text-anchor="middle">NALVI</text>
      <text class="tagline" x="100" y="36" font-size="20" text-anchor="middle">HANDMADE NATURAL SOAP</text>
      <line class="rule" x1="-15" y1="48" x2="215" y2="48"/>
      <text class="ingredients" x="100" y="80" font-size="24" text-anchor="middle">with Seabuckthorn &amp; Olive oil</text>
    </g>
  </g>

  <!-- left side label -->
  <g class="label on-white">
    <rect class="frame-outer" x="58" y="705" width="178" height="345" rx="40"/>
    <rect class="frame-white" x="72" y="722" width="150" height="311" rx="28"/>
    <g transform="translate(147,877) rotate(90)">
      <text class="brand" x="48" y="-3" font-size="40" text-anchor="middle">NALVI</text>
      <text class="tagline" x="48" y="19" font-size="10" text-anchor="middle">HANDMADE NATURAL SOAP</text>
      <line class="rule" x1="-12" y1="26" x2="108" y2="26"/>
      <text class="ingredients" x="48" y="38" font-size="11" text-anchor="middle">with Seabuckthorn &amp; Olive oil</text>
    </g>
  </g>

  <!-- right side label -->
  <g class="label on-green">
    <rect class="frame-outer" x="988" y="960" width="172" height="340" rx="40"/>
    <rect class="frame-green" x="1002" y="977" width="144" height="306" rx="28"/>
    <g transform="translate(1075,1130) rotate(-90)">
      <text class="brand" x="55" y="-3" font-size="40" text-anchor="middle">NALVI</text>
      <text class="tagline" x="55" y="17" font-size="10" text-anchor="middle">HANDMADE NATURAL SOAP</text>
      <line class="rule" x1="-5" y1="24" x2="115" y2="24"/>
      <text class="ingredients" x="55" y="38" font-size="11" text-anchor="middle">with Seabuckthorn &amp; Olive oil</text>
    </g>
  </g>
</svg>
</body>
</html>
```